Managed IT services business card design

We haven't needed a business card since the founding of the business in 2005. All our clients have been coming through word of mouth. And lately more and more existing clients are requesting for our business cards to pass on to their contacts in recommending us.
So we needing a business card design. We use various innovative solutions and methodologies to provide IT services to small businesses in managing their IT systems. Our role is the same as an in-house, full-time IT Manager for our clients, but outsourced. So we take care of all our clients' IT needs, just as an IT Manager would be expected to perform.
We have a holding website, which we're happy to leave for now. If we can use the same logo would be great - www.lomvex.com.au
Preferred colours are shades of are white, grey and black.
We pride our business with the following traits: proactive, good service, prompt response, trustworthy.
Target Market(s)
Small businesses of any industry
Industry/Entity Type
Business

```html
<!DOCTYPE html>
<html lang="en">
<head>
<meta charset="utf-8">
<title>Lomvex business card</title>
<link rel="stylesheet" href="https://fonts.googleapis.com/css2?family=Questrial&display=swap">
<style>
  :root {
    --backdrop: #e4e4e4;
    --card: #151313;
    --ink: #ffffff;
    --ink-soft: #d8d8d8;
    --divider: #8a8a8a;
    --shadow: rgba(0, 0, 0, 0.28);
  }
  * { box-sizing: border-box; margin: 0; padding: 0; }
  html, body {
    width: 1200px;
    height: 680px;
    overflow: hidden;
    background: var(--backdrop);
    font-family: "Questrial", sans-serif;
    color: var(--ink);
  }
  .sheet {
    position: relative;
    width: 1200px;
    height: 680px;
    display: flex;
    align-items: center;
    justify-content: center;
    gap: 50px;
  }
  .card {
    position: relative;
    width: 525px;
    height: 300px;
    background: var(--card);
    box-shadow: 0 8px 22px var(--shadow);
  }

  /* Front */
  .card--front .brand {
    position: absolute;
    right: 46px;
    bottom: 66px;
    text-align: right;
  }
  .brand__name {
    display: flex;
    align-items: center;
    gap: 16px;
    font-size: 46px;
    letter-spacing: 0.22em;
    line-height: 1;
  }
  .brand__dot {
    width: 12px;
    height: 12px;
    border-radius: 50%;
    background: var(--ink);
  }
  .brand__url {
    margin-top: 14px;
    font-size: 15px;
    letter-spacing: 0.32em;
    color: var(--ink-soft);
    padding-right: 28px;
  }

  /* Back */
  .card--back {
    display: flex;
    align-items: center;
  }
  .card--back .brand {
    width: 262px;
    padding-left: 36px;
  }
  .card--back .brand__name {
    font-size: 36px;
    gap: 12px;
  }
  .card--back .brand__dot { width: 10px; height: 10px; }
  .divider {
    width: 1px;
    height: 170px;
    background: linear-gradient(to bottom, transparent, var(--divider) 35%, var(--divider) 65%, transparent);
  }
  .contact {
    padding-left: 26px;
    font-size: 14px;
    line-height: 1.3;
    color: var(--ink);
  }
  .contact__name { font-size: 17px; }
  .contact__role { font-size: 13px; color: var(--ink-soft); margin-left: 14px; }
  .contact__address { margin: 14px 0 12px 30px; }
  .contact__list { list-style: none; }
  .contact__item {
    display: flex;
    align-items: center;
    gap: 10px;
    margin-bottom: 1px;
  }
  .contact__icon { width: 13px; height: 13px; flex: none; }
</style>
</head>
<body>
<main class="sheet">
  <section class="card card--front" aria-label="Card front">
    <div class="brand">
      <div class="brand__name">lomvex<span class="brand__dot"></span></div>
      <div class="brand__url">www.lomvex.com</div>
    </div>
  </section>

  <section class="card card--back" aria-label="Card back">
    <div class="brand">
      <div class="brand__name">lomvex<span class="brand__dot"></span></div>
    </div>
    <div class="divider"></div>
    <div class="contact">
      <div class="contact__name">Mark Tellan</div>
      <div class="contact__role">director</div>
      <div class="contact__address">1840 Corlow Ave<br>Denham TX 78100</div>
      <ul class="contact__list">
        <li class="contact__item">
          <svg class="contact__icon" viewBox="0 0 16 16" aria-hidden="true"><path fill="#fff" d="M4 1l3 3-2 2c1 2 3 4 5 5l2-2 3 3-2 3C7 15 1 9 1 3z"/></svg>
          512 004 2710
        </li>
        <li class="contact__item">
          <svg class="contact__icon" viewBox="0 0 16 16" aria-hidden="true"><rect x="4" y="1" width="8" height="5" fill="none" stroke="#fff" stroke-width="1.5"/><rect x="1" y="6" width="14" height="8" rx="1" fill="#fff"/></svg>
          512 004 2711
        </li>
        <li class="contact__item">
          <svg class="contact__icon" viewBox="0 0 16 16" aria-hidden="true"><rect x="1" y="3" width="14" height="10" fill="#fff"/><path d="M1 3l7 6 7-6" fill="none" stroke="#151313" stroke-width="1.4"/></svg>
          info@lomvex.com
        </li>
        <li class="contact__item">
          <svg class="contact__icon" viewBox="0 0 16 16" aria-hidden="true"><circle cx="8" cy="8" r="7" fill="#fff"/><path d="M1 8h14M8 1c-3 4-3 10 0 14M8 1c3 4 3 10 0 14" fill="none" stroke="#151313" stroke-width="0.9"/></svg>
          www.lomvex.com
        </li>
      </ul>
    </div>
  </section>
</main>
</body>
</html>
```